Inviting A6 Flyer for Church membership

We need an A6 size flyer for the church. We are looking for something fresh, inviting and impactful. Church new logo and current flyer design attached.
Back text as follows:
We would love to have you join us as our SPECIAL GUEST this Sunday at 10am.
You can find us at Harvest Lantern Family Church, 17-19 Marlow Crest Road
(Behind Dunholt Grocers), Thornbury Meadow Village,QX4 7LB
For more information or for a chat, please call us on 07700 900418 / 07700 900752 or email church@hlfcuk-mail.test
Target Market(s)
Church
Industry/Entity Type
Church
Colors
Designer to choose colors to be used in the design.
Requirements
Must have
- fresh, inviting and impactful.
- Chruch logo (attached)
Should not have
- Too much going on

```html
<!DOCTYPE html>
<html lang="en">
<head>
<meta charset="utf-8">
<title>Be Our Guest – A6 Flyer</title>
<link rel="stylesheet" href="https://fonts.googleapis.com/css2?family=Cinzel:wght@400;600;700&family=Marcellus&family=Montserrat:wght@800&family=Lato:wght@700&display=swap">
<style>
  :root {
    --backdrop: #2b2b2d;
    --blue: #1677bd;
    --blue-deep: #0c5c9e;
    --red: #a52f1c;
    --navy: #1c5d9c;
    --ink: #161616;
    --white: #ffffff;
    --paper: #f2f2f3;
  }
  * { box-sizing: border-box; margin: 0; padding: 0; }
  html, body { width: 1200px; height: 902px; overflow: hidden; }
  body { background: var(--backdrop); position: relative; }

  .flyer {
    position: absolute;
    overflow: hidden;
    box-shadow: 0 6px 18px rgba(0,0,0,.45);
  }
  .flyer--front { left: 63px; top: 78px; width: 505px; height: 712px; border-left: 3px solid var(--red); }
  .flyer--back  { left: 624px; top: 145px; width: 508px; height: 716px; background: var(--paper); }

  .flyer__shape { position: absolute; inset: 0; width: 100%; height: 100%; }

  .photo-area { position: absolute; left: 0; top: 0; width: 100%; }
  .photo-area--interior {
    height: 440px;
    background:
      radial-gradient(ellipse 90px 110px at 95px 165px, rgba(255,255,255,.85), rgba(255,255,255,0) 100%),
      linear-gradient(160deg, #8a7b6c 0%, #5a4c40 35%, #7b6b5b 60%, #4a3d33 100%);
  }
  .photo-area--pews {
    height: 520px;
    background: linear-gradient(180deg, #f4f4f5 0%, #e6e6e8 45%, #d3d3d6 75%, #c9c9cc 100%);
  }

  .emblem {
    position: absolute;
    background: var(--white);
    border: 5px solid var(--red);
    border-radius: 50%;
    display: flex;
    flex-direction: column;
    align-items: center;
    justify-content: center;
    gap: 10px;
  }
  .flyer--front .emblem { left: 141px; top: 268px; width: 218px; height: 218px; }
  .flyer--back  .emblem { left: 155px; top: 322px; width: 200px; height: 200px; }
  .emblem__mark { width: 46px; height: 46px; border-radius: 50%; background: var(--blue); }
  .emblem__name {
    font-family: "Marcellus", serif;
    color: var(--red);
    font-size: 15px;
    line-height: 1.15;
    text-align: center;
    letter-spacing: .02em;
  }

  .front-title {
    position: absolute;
    left: 0; width: 100%;
    text-align: center;
    color: var(--white);
    font-family: "Cinzel", serif;
    font-weight: 400;
    line-height: 1;
    white-space: nowrap;
  }
  .front-title__lead { top: 508px; font-size: 64px; }
  .front-title__main { top: 569px; font-size: 128px; }

  .invite {
    position: absolute;
    left: 0; top: 62px; width: 100%;
    text-align: center;
    font-family: "Cinzel", serif;
    font-weight: 700;
    color: var(--navy);
    font-size: 27px;
    line-height: 32px;
  }
  .service-time {
    position: absolute;
    left: 34px; top: 168px; width: 440px; height: 36px;
    background: var(--red);
    border-radius: 18px;
    color: var(--white);
    font-family: "Montserrat", sans-serif;
    font-weight: 800;
    font-size: 28px;
    line-height: 36px;
    text-align: center;
  }
  .address {
    position: absolute;
    left: 0; top: 212px; width: 100%;
    text-align: center;
    font-family: "Lato", sans-serif;
    font-weight: 700;
    color: var(--ink);
    font-size: 18px;
    line-height: 23px;
  }
  .address__note { font-size: 16px; }

  .contact {
    position: absolute;
    left: 0; top: 535px; width: 100%;
    text-align: center;
    color: var(--white);
  }
  .contact__lead {
    font-family: "Cinzel", serif;
    font-weight: 600;
    font-size: 21px;
    line-height: 27px;
    letter-spacing: .03em;
  }
  .contact__call, .contact__line {
    font-family: "Lato", sans-serif;
    font-weight: 700;
  }
  .contact__call { font-size: 23px; margin-top: 6px; line-height: 30px; }
  .contact__line { font-size: 19px; line-height: 32px; display: flex; justify-content: center; align-items: center; gap: 7px; }
  .contact__icon { width: 14px; height: 14px; }
</style>
</head>
<body>

<section class="flyer flyer--front" aria-label="Flyer front">
  <div class="photo-area photo-area--interior" role="img" aria-label="Photograph of an ornate cathedral interior with light streaming through a window"></div>
  <svg class="flyer__shape" viewBox="0 0 505 712" preserveAspectRatio="none" aria-hidden="true">
    <defs>
      <linearGradient id="frontBlue" x1="0" y1="0" x2="0" y2="1">
        <stop offset="0" stop-color="#1a7fc4"/>
        <stop offset="1" stop-color="#0c5c9e"/>
      </linearGradient>
    </defs>
    <path d="M0 402 Q252 355 505 402 L505 712 L0 712 Z" fill="#a52f1c"/>
    <path d="M0 410 Q252 364 505 410 L505 712 L0 712 Z" fill="url(#frontBlue)"/>
  </svg>
  <div class="emblem">
    <span class="emblem__mark"></span>
    <p class="emblem__name">HARVEST LANTERN<br>MINISTRIES</p>
  </div>
  <h1 class="front-title front-title__lead">BE OUR</h1>
  <p class="front-title front-title__main">GUEST</p>
</section>

<section class="flyer flyer--back" aria-label="Flyer back">
  <div class="photo-area photo-area--pews" role="img" aria-label="Faint photograph of a church interior with pews"></div>
  <svg class="flyer__shape" viewBox="0 0 508 716" preserveAspectRatio="none" aria-hidden="true">
    <defs>
      <linearGradient id="backBlue" x1="0" y1="0" x2="0" y2="1">
        <stop offset="0" stop-color="#1a7fc4"/>
        <stop offset="1" stop-color="#0c5c9e"/>
      </linearGradient>
    </defs>
    <path d="M0 490 Q254 418 508 490 L508 716 L0 716 Z" fill="#a52f1c"/>
    <path d="M0 499 Q254 428 508 499 L508 716 L0 716 Z" fill="url(#backBlue)"/>
  </svg>

  <h2 class="invite">WE WOULD<br>LOVE TO HAVE YOU JOIN US<br>AS OUR SPECIAL GUEST</h2>
  <p class="service-time">THIS SUNDAY AT 10AM.</p>
  <p class="address">You can find us at Harvest Lantern Family<br>Church, 17-19 Marlow Crest Road <span class="address__note">(Behind Dunholt Grocers)</span>,<br>Thornbury Meadow Village,QX4 7LB</p>

  <div class="emblem">
    <span class="emblem__mark"></span>
    <p class="emblem__name">HARVEST LANTERN<br>MINISTRIES</p>
  </div>

  <div class="contact">
    <p class="contact__lead">FOR MORE INFORMATION<br>OR FOR A CHAT</p>
    <p class="contact__call">Please call us on</p>
    <p class="contact__line">
      <svg class="contact__icon" viewBox="0 0 16 16" aria-hidden="true"><circle cx="8" cy="8" r="7" fill="none" stroke="#fff" stroke-width="1.6"/><path d="M5.4 4.5l1.3 1.6-.7 1c.5 1 1.3 1.8 2.3 2.3l1-.7 1.6 1.3-.8 1.2c-2.8-.5-4.8-2.5-5.3-5.3z" fill="#fff"/></svg>
      07700 900418 / 07700 900752
    </p>
    <p class="contact__line">
      <svg class="contact__icon" viewBox="0 0 16 16" aria-hidden="true"><rect x="1" y="3.5" width="14" height="9" fill="#fff"/><path d="M1 3.5l7 5 7-5" fill="none" stroke="#1677bd" stroke-width="1.3"/></svg>
      church@hlfcuk-mail.test
    </p>
  </div>
</section>

</body>
</html>
```